Pitch Deck Foundation ÉlanJeu

ÉlanJeu is one of the largest non-profit organizations in Switzerland, which has been organizing free sports activities for children and young people for 25 years. We are active in the field of child and youth development in Switzerland and use sport as a means of addiction prevention, health promotion and social integration. With our programs, we open up vacant spaces for sports and encounters, creating the conditions for regular meeting places across cultural and social boundaries.

This presentation is to be given a new, modern design. It will be used when pitching to organizations with the goal of resulting in sponsoring partnerships and raising more donations

The pitch presentation should be structured in the following chapters: Intro (page 2-3), Facts and Figures (page 4-5), Topic Areas (page 6-14), Partnership Model (page 15-17), Closing (page 18-19).

Please make the colors and design according to the CI/CD, which was uploaded separately.

The goal is to arouse emotions with images.

Please make sure, that graphics display legibly.

Format 16:9

```html
<!DOCTYPE html>
<html lang="en">
<head>
<meta charset="utf-8">
<title>Pitch Deck – Foundation ÉlanJeu</title>
<link href="https://fonts.googleapis.com/css2?family=Montserrat:wght@400;500;600;700;800&display=swap" rel="stylesheet">
<style>
  :root {
    --brand-blue: #00a8e1;
    --brand-blue-soft: #d6eefa;
    --brand-red: #e8505b;
    --ink: #1d1d1f;
    --page: #eeeff1;
    --slide: #ffffff;
    --grey-soft: #f1f1f2;
  }
  * { box-sizing: border-box; margin: 0; padding: 0; }
  html, body { width: 1200px; height: 800px; overflow: hidden; }
  body {
    background: var(--page);
    font-family: "Montserrat", Arial, sans-serif;
    color: var(--ink);
    position: relative;
  }
  .slide {
    position: absolute;
    width: 493px;
    height: 277px;
    background: var(--slide);
    overflow: hidden;
  }
  .slide--cover { left: 70px; top: 109px; }
  .slide--hanging { left: 589px; top: 107px; }
  .slide--labor { left: 70px; top: 412px; }
  .slide--foundation { left: 589px; top: 412px; }

  .backdrop {
    position: absolute;
    right: 0;
    bottom: 0;
    width: 230px;
    height: 140px;
  }
  .backdrop--blue { background: radial-gradient(ellipse 70% 60% at 85% 100%, var(--brand-blue-soft) 0%, rgba(255,255,255,0) 75%); }
  .backdrop--grey { background: radial-gradient(ellipse 70% 60% at 85% 100%, var(--grey-soft) 0%, rgba(255,255,255,0) 75%); }

  .brand {
    position: absolute;
    display: flex;
    align-items: center;
    gap: 3px;
    color: var(--brand-blue);
    font-weight: 700;
    white-space: nowrap;
  }
  .brand__mark { background: var(--brand-blue); display: block; }
  .brand--corner { right: 13px; top: 15px; font-size: 9px; }
  .brand--corner .brand__mark { width: 8px; height: 8px; }

  .title {
    position: absolute;
    left: 26px;
    top: 20px;
    color: var(--brand-blue);
    font-weight: 700;
    font-size: 15.5px;
    line-height: 18.5px;
    letter-spacing: 0.2px;
    text-transform: uppercase;
  }
  .title-bar {
    position: absolute;
    left: 0;
    top: 24px;
    width: 19px;
    height: 11px;
    background: var(--brand-blue);
  }
  .page-number {
    position: absolute;
    right: 15px;
    bottom: 12px;
    font-size: 8px;
    color: var(--brand-blue);
  }
  .photo { position: absolute; display: block; }

  /* Cover */
  .cover__photo {
    right: 0; top: 0; width: 340px; height: 277px;
    background: radial-gradient(ellipse 55% 65% at 58% 42%, #dcc6b6 0%, #c8d7ea 45%, #d9ecf8 70%, rgba(255,255,255,0) 100%);
  }
  .cover__brand { left: 48px; top: 86px; font-size: 17px; gap: 6px; }
  .cover__brand .brand__mark { width: 18px; height: 18px; }
  .cover__kicker { position: absolute; left: 47px; top: 116px; font-size: 17px; font-weight: 500; color: var(--brand-blue); }
  .cover__name { position: absolute; left: 47px; top: 136px; font-size: 18px; font-weight: 800; color: var(--brand-blue); }
  .cover__date { position: absolute; left: 47px; top: 159px; font-size: 9.5px; color: var(--brand-blue); }
  .cover__link { position: absolute; left: 48px; top: 183px; display: flex; align-items: center; gap: 7px; font-size: 8.5px; font-weight: 600; color: var(--brand-red); text-decoration: underline; }
  .cover__link-icon { width: 13px; height: 13px; background: var(--brand-red); display: flex; align-items: center; justify-content: center; }

  /* Hanging around */
  .compare { position: absolute; top: 59px; width: 159px; height: 159px; border: 1.5px solid var(--brand-blue); }
  .compare--earlier { left: 48px; }
  .compare--today { left: 285px; }
  .compare .photo { left: 4px; top: 4px; right: 4px; bottom: 4px; }
  .compare--earlier .photo { background: linear-gradient(180deg, #c9c9c9 0%, #7d7d7d 55%, #4a4a4a 100%); }
  .compare--today .photo { background: linear-gradient(160deg, #6f6a66 0%, #a7a4a9 40%, #3d4e6e 80%, #e6e2dc 100%); }
  .compare__tag {
    position: absolute; top: -1px; left: 50%; transform: translateX(-50%);
    width: 77px; height: 15px; background: var(--brand-red); color: #fff;
    font-size: 9px; font-weight: 600; text-align: center; line-height: 15px; letter-spacing: 0.3px;
  }
  .versus {
    position: absolute; left: 231px; top: 123px; width: 31px; height: 31px;
    background: var(--brand-blue); color: #fff; font-weight: 700; font-size: 11px;
    display: flex; align-items: center; justify-content: center;
  }
  .hanging__caption { position: absolute; left: 0; right: 0; top: 231px; text-align: center; font-size: 7.6px; font-weight: 700; }

  /* Labor market */
  .labor__text { position: absolute; left: 26px; top: 88px; width: 252px; font-size: 8.8px; line-height: 11.2px; }
  .labor__text p + p { margin-top: 3px; }
  .labor__accent { color: var(--brand-blue); font-weight: 700; }
  .stat { position: absolute; left: 26px; top: 158px; width: 187px; height: 42px; border: 1.5px solid var(--brand-red); display: flex; }
  .stat__value { width: 43px; background: var(--brand-red); color: #fff; font-size: 14px; font-weight: 700; display: flex; align-items: center; justify-content: center; }
  .stat__label { padding: 8px 0 0 14px; font-size: 8.8px; font-weight: 700; line-height: 11px; }
  .stat__label span { color: var(--brand-blue); }
  .labor__frame { position: absolute; left: 348px; top: 81px; width: 145px; height: 126px; border: 1.5px solid var(--brand-blue); }
  .labor__photo { left: 328px; top: 88px; width: 165px; height: 111px; background: linear-gradient(110deg, #6b6a62 0%, #2a2a28 30%, #171717 70%, #3a342e 100%); }

  /* Foundation */
  .foundation__side { position: absolute; left: 0; top: 68px; width: 12px; height: 91px; border: 1.5px solid var(--brand-blue); border-left: none; }
  .foundation__hall { left: 19px; top: 68px; width: 91px; height: 91px; background: linear-gradient(180deg, #cdb99a 0%, #b9a58a 22%, #35b6e6 38%, #1fa6dc 100%); }
  .foundation__lead { position: absolute; left: 121px; top: 67px; width: 320px; font-size: 9.2px; line-height: 11px; }
  .foundation__list { position: absolute; left: 131px; top: 102px; width: 270px; list-style: none; font-size: 7.5px; line-height: 10px; }
  .foundation__list li { position: relative; padding-left: 8px; margin-bottom: 3.8px; }
  .foundation__list li::before { content: ""; position: absolute; left: -1px; top: 2.5px; width: 4px; height: 4px; background: var(--brand-red); }
  .foundation__kids { left: 143px; top: 172px; width: 244px; height: 85px; background: linear-gradient(90deg, #9f8f7a 0%, #d8c6ad 30%, #e06a9a 45%, #c9b294 60%, #5b8fd0 75%, #c7b39c 100%); }
  .foundation__band { position: absolute; left: 143px; top: 265px; width: 244px; height: 12px; background: var(--brand-blue); }
</style>
</head>
<body>

  <section class="slide slide--cover">
    <div class="photo cover__photo" role="img" aria-label="Portrait photo of a smiling child fading into soft blue brand waves"></div>
    <div class="brand cover__brand"><span class="brand__mark"></span>ÉlanJeu</div>
    <div class="cover__kicker">Pitch Deck</div>
    <div class="cover__name">Foundation ÉlanJeu</div>
    <div class="cover__date">May 2023</div>
    <div class="cover__link">
      <span class="cover__link-icon">
        <svg width="9" height="9" viewBox="0 0 10 10" aria-hidden="true"><circle cx="5" cy="5" r="4" fill="none" stroke="#fff" stroke-width="0.9"/><ellipse cx="5" cy="5" rx="1.8" ry="4" fill="none" stroke="#fff" stroke-width="0.8"/><line x1="1" y1="5" x2="9" y2="5" stroke="#fff" stroke-width="0.8"/></svg>
      </span>
      www.elanjeu.ch
    </div>
  </section>

  <section class="slide slide--hanging">
    <div class="backdrop backdrop--blue" role="img" aria-label="Soft blue decorative wave area"></div>
    <span class="title-bar"></span>
    <h2 class="title">Hanging around</h2>
    <div class="brand brand--corner"><span class="brand__mark"></span>ÉlanJeu</div>
    <div class="compare compare--earlier">
      <div class="photo" role="img" aria-label="Black and white photo of children hanging upside down from a bar outdoors"></div>
      <div class="compare__tag">EARLIER</div>
    </div>
    <div class="versus">VS</div>
    <div class="compare compare--today">
      <div class="photo" role="img" aria-label="Photo of children sitting on a sofa playing video games"></div>
      <div class="compare__tag">TODAY</div>
    </div>
    <p class="hanging__caption">This has serious effects on health (overweight, psychological problems etc.)</p>
    <span class="page-number">1</span>
  </section>

  <section class="slide slide--labor">
    <div class="backdrop backdrop--grey" role="img" aria-label="Soft grey decorative wave area"></div>
    <span class="title-bar"></span>
    <h2 class="title">More difficult entry into<br>the labor market and adult world</h2>
    <div class="brand brand--corner"><span class="brand__mark"></span>ÉlanJeu</div>
    <div class="labor__text">
      <p>The transition from school to vocational education is complex and challenging.</p>
      <p><span class="labor__accent">The consequences:</span> Orientation difficulties and excessive demands; especialy for young people from disadvantaged families or with learning difficulties.</p>
    </div>
    <div class="stat">
      <div class="stat__value">30%</div>
      <div class="stat__label">16 to 24 year olds are<br><span>emotionally exhausted</span></div>
    </div>
    <div class="labor__frame"></div>
    <div class="photo labor__photo" role="img" aria-label="Photo of a tired young person resting his head on a desk by a window"></div>
    <span class="page-number">1</span>
  </section>

  <section class="slide slide--foundation">
    <div class="backdrop backdrop--grey" role="img" aria-label="Soft grey decorative wave area"></div>
    <span class="title-bar"></span>
    <h2 class="title">Foundation ÉlanJeu</h2>
    <div class="brand brand--corner"><span class="brand__mark"></span>ÉlanJeu</div>
    <div class="foundation__side"></div>
    <div class="photo foundation__hall" role="img" aria-label="Photo of a sports hall with blue floor and young people playing table tennis"></div>
    <p class="foundation__lead">We have been opening vacant sports halls for children and young people <strong>since 1999</strong>.</p>
    <ul class="foundation__list">
      <li>Low-threshold and regular meeting places, for movement and encounter projects.</li>
      <li>Different programs for all ages</li>
      <li>Led by specially trained youth coaches.</li>
      <li>Promotion of health, equal opportuntites and integrantion.</li>
    </ul>
    <div class="photo foundation__kids" role="img" aria-label="Photo of children playing with balloons in a gym"></div>
    <div class="foundation__band"></div>
    <span class="page-number">1</span>
  </section>

</body>
</html>
```